The Pipe Lantern business cards

Hi
i have attached a photo, this is how i want the front of my business card to look like:
i want the water drop on the right to be orange
and the water drop on the left to be gloss black
"The" and "Pty Ltd." will be in the same orange as the water drop
and "Pipe Lantern" will be in white
The background of the logo will be a matte black
on the back of the business card i need the following info:
'The Pipe Lantern pty ltd. '
'Plumbing . Drainage . Gas Fitting . Roofing . Jet Blasting . CCTV . '
Also my contact details:
Cal Yardley
0418672913
thepipelantern@mailkestrel.com
Licence# 583016K
Target Market(s)
Strata managers, building managers, the general public
Industry/Entity Type
Business

```html
<!DOCTYPE html>
<html lang="en">
<head>
<meta charset="utf-8">
<title>The Pipe Lantern – Business Cards</title>
<link href="https://fonts.googleapis.com/css2?family=Raleway:wght@400;500;600;700&display=swap" rel="stylesheet">
<style>
  :root {
    --backdrop: #c8c6c7;
    --card-matte: #1b1b1b;
    --card-deep: #060606;
    --orange: #ee8b2a;
    --white: #ffffff;
    --divider: #2a2a2a;
    --dot: #050505;
    --sep: #3a3a3a;
  }
  * { box-sizing: border-box; margin: 0; padding: 0; }
  html, body { width: 982px; height: 1200px; overflow: hidden; }
  body {
    background: var(--backdrop);
    font-family: "Raleway", sans-serif;
    position: relative;
  }
  .card {
    position: absolute;
    left: 98px;
    width: 786px;
    height: 449px;
    border-radius: 34px;
    background: var(--card-matte);
    overflow: hidden;
  }
  .card--front { top: 135px; }
  .card--back { top: 615px; }

  /* Brand lockup */
  .brand {
    position: absolute;
    display: flex;
    align-items: center;
    color: var(--white);
    font-weight: 400;
  }
  .brand__circle {
    border: solid var(--orange);
    border-radius: 50%;
    flex: none;
  }
  .brand__name { line-height: 1; text-transform: uppercase; }
  .brand__name span { display: block; }

  .card--front .brand { left: 113px; top: 130px; gap: 44px; }
  .card--front .brand__circle { width: 150px; height: 150px; border-width: 6px; }
  .card--front .brand__name { font-size: 34px; letter-spacing: 4px; }
  .card--front .brand__name .brand__main { font-size: 62px; letter-spacing: 2px; margin: 8px 0; }

  .card--back .brand { left: 268px; top: 52px; gap: 22px; }
  .card--back .brand__circle { width: 66px; height: 66px; border-width: 3px; }
  .card--back .brand__name { font-size: 16px; letter-spacing: 2px; }
  .card--back .brand__name .brand__main { font-size: 30px; letter-spacing: 1px; margin: 4px 0; }

  /* Services */
  .services {
    position: absolute;
    top: 183px;
    left: 0; right: 0;
    display: flex;
    justify-content: center;
    gap: 20px;
    list-style: none;
    color: var(--white);
    font-size: 19px;
    font-weight: 500;
  }
  .services li { display: flex; align-items: center; gap: 6px; }
  .services li::before {
    content: "";
    width: 12px; height: 12px;
    border-radius: 50%;
    background: var(--dot);
  }
  .sectors {
    position: absolute;
    top: 220px;
    left: 0; right: 0;
    text-align: center;
    color: var(--orange);
    font-size: 13.5px;
    font-weight: 600;
    letter-spacing: 0.3px;
  }
  .sectors .sep { color: var(--sep); margin: 0 8px; }

  .hours-band {
    position: absolute;
    top: 281px; left: 0; right: 0;
    height: 27px;
    background: var(--orange);
    color: #111;
    font-size: 14px;
    font-weight: 700;
    text-align: center;
    line-height: 27px;
    z-index: 2;
  }
  .hours-band::after {
    content: "";
    position: absolute;
    left: 50%; bottom: -7px;
    transform: translateX(-50%);
    border: 7px solid transparent;
    border-bottom: 0;
    border-top-color: var(--orange);
  }
  .contact-panel {
    position: absolute;
    top: 308px; left: 0; right: 0; bottom: 0;
    background: var(--card-deep);
  }
  .person {
    position: absolute;
    right: 420px;
    top: 49px;
    text-align: right;
  }
  .person__name {
    color: var(--orange);
    font-size: 27px;
    font-weight: 400;
    letter-spacing: 2px;
    line-height: 1;
  }
  .person__licence {
    color: var(--white);
    font-size: 13px;
    letter-spacing: 0.5px;
    margin-top: 3px;
  }
  .contact-divider {
    position: absolute;
    left: 393px; top: 30px;
    width: 1px; height: 82px;
    background: var(--divider);
  }
  .contacts {
    position: absolute;
    left: 420px; top: 35px;
    list-style: none;
    color: var(--white);
    font-size: 17.5px;
    letter-spacing: 0.4px;
  }
  .contacts li { display: flex; align-items: center; gap: 8px; height: 25px; }
  .contacts svg { width: 16px; height: 16px; fill: var(--orange); flex: none; }
</style>
</head>
<body>

<section class="card card--front">
  <div class="brand">
    <div class="brand__circle"></div>
    <div class="brand__name">
      <span>The</span>
      <span class="brand__main">Pipe Lantern</span>
      <span>Pty Ltd.</span>
    </div>
  </div>
</section>

<section class="card card--back">
  <div class="brand">
    <div class="brand__circle"></div>
    <div class="brand__name">
      <span>The</span>
      <span class="brand__main">Pipe Lantern</span>
      <span>Pty Ltd.</span>
    </div>
  </div>

  <ul class="services">
    <li>Plumbing</li>
    <li>Drainage</li>
    <li>Gas Fitting</li>
    <li>Roofing</li>
    <li>Jet Blasting</li>
    <li>CCTV</li>
  </ul>
  <p class="sectors">DOMESTIC<span class="sep">::</span>COMMERCIAL<span class="sep">::</span>INDUSTRIAL<span class="sep">::</span>MAINTENANCE</p>

  <div class="hours-band">24 HOURS A DAY / 7 DAYS A WEEK</div>

  <div class="contact-panel">
    <div class="person">
      <p class="person__name">CAL YARDLEY</p>
      <p class="person__licence">Licence# 583016K</p>
    </div>
    <div class="contact-divider"></div>
    <ul class="contacts">
      <li>
        <svg viewBox="0 0 16 16" aria-hidden="true"><path d="M1 5c0-2 3-3 7-3s7 1 7 3v1.5h-3.5V5h-7v1.5H1z M4 8l2-2h4l2 2v5H4z M8 8.5a1.8 1.8 0 1 0 0.01 0z"/></svg>
        0418672913
      </li>
      <li>
        <svg viewBox="0 0 16 16" aria-hidden="true"><path d="M1 3h14v1.2L8 9 1 4.2z M1 6l7 4.8L15 6v7H1z"/></svg>
        thepipelantern@mailkestrel.com
      </li>
      <li>
        <svg viewBox="0 0 16 16" aria-hidden="true"><rect x="1" y="1" width="14" height="14" rx="2"/></svg>
        pagenook.com/thepipelantern
      </li>
    </ul>
  </div>
</section>

</body>
</html>
```